Solace Chiropractic & Acupuncture Business Cards

I need a business card design that feels elevated. I am open to any of the logo designs uploaded. We have two doctors so I'll need to be able to change out the names.

Information:
Marnie Toller D.C., L.Ac., MSOM
584 W 12th St, Ste 320
Larkfield, NE 68419
solacegrove.net
620-555-0147
drmarnie@solacegrove.com
Updates

We have designs we like now, we are just trying to choose between top contenders. Thanks for your submissions!

Contact Information for Business Card

noted in description

Requirements
Must have
• ability to edit info if possible
Nice to have
• Please see our website solacegrove.net for our style and colors

```html
<!DOCTYPE html>
<html lang="en">
<head>
<meta charset="utf-8">
<title>Solace Chiropractic &amp; Acupuncture — Business Cards</title>
<link href="https://fonts.googleapis.com/css2?family=Tinos&display=swap" rel="stylesheet">
<style>
  :root {
    --backdrop: #1c1c1c;
    --card: #5f7a87;
    --ink: #ffffff;
    --icon: #e6e9eb;
  }
  * { margin: 0; padding: 0; box-sizing: border-box; }
  html, body {
    width: 1200px; height: 1059px; overflow: hidden;
    background: var(--backdrop);
    font-family: "Tinos", "Times New Roman", serif;
    color: var(--ink);
  }
  .canvas { position: relative; width: 1200px; height: 1059px; }
  .card {
    position: absolute;
    background: var(--card);
    border-radius: 24px;
  }
  .card--front { left: 256px; top: 87px; width: 692px; height: 395px; }
  .card--back  { left: 256px; top: 549px; width: 701px; height: 400px; }

  .wordmark { position: absolute; text-align: right; line-height: 1; font-weight: 400; }
  .wordmark__name { display: block; }
  .wordmark__tagline { display: block; text-transform: uppercase; }

  .card--front .wordmark { right: 39px; top: 62px; }
  .card--front .wordmark__name { font-size: 96px; letter-spacing: -1px; }
  .card--front .wordmark__tagline { font-size: 13px; letter-spacing: 0.5px; margin-top: 8px; }

  .card--back .wordmark { right: 107px; top: 118px; }
  .card--back .wordmark__name { font-size: 168px; letter-spacing: -2px; }
  .card--back .wordmark__tagline { font-size: 21px; letter-spacing: 0.8px; margin-top: 10px; }

  .divider {
    position: absolute; left: 43px; top: 266px; width: 584px; height: 1.5px;
    background: var(--ink);
  }
  .contact-list { position: absolute; left: 35px; top: 284px; list-style: none; }
  .contact-list li {
    display: flex; align-items: center; height: 29px;
    font-size: 17.5px; letter-spacing: 0.2px;
  }
  .contact-list svg { width: 20px; height: 20px; margin-right: 11px; fill: var(--icon); flex: none; }

  .practitioner {
    position: absolute; right: 65px; top: 294px;
    text-align: right; font-size: 17.5px; line-height: 21.5px; letter-spacing: 0.2px;
    font-style: normal;
  }
</style>
</head>
<body>
<main class="canvas">
  <section class="card card--front">
    <div class="wordmark">
      <span class="wordmark__name">Solace</span>
      <span class="wordmark__tagline">Chiropractic &amp; Acupuncture</span>
    </div>
    <div class="divider"></div>
    <ul class="contact-list">
      <li>
        <svg viewBox="0 0 24 24" aria-hidden="true"><path d="M6.6 10.8a15.1 15.1 0 0 0 6.6 6.6l2.2-2.2c.3-.3.7-.4 1-.2 1.1.4 2.3.6 3.6.6.6 0 1 .4 1 1V20c0 .6-.4 1-1 1A17 17 0 0 1 3 4c0-.6.4-1 1-1h3.5c.6 0 1 .4 1 1 0 1.3.2 2.5.6 3.6.1.3 0 .7-.2 1z"/></svg>
        620-555-0147
      </li>
      <li>
        <svg viewBox="0 0 24 24" aria-hidden="true"><path d="M2 5h20l-10 8z"/><path d="M2 7l10 8 10-8v12H2z"/></svg>
        drmarnie@solacegrove.com
      </li>
      <li>
        <svg viewBox="0 0 24 24" aria-hidden="true"><path d="M12 2a10 10 0 1 0 0 20 10 10 0 0 0 0-20zm-1 17.9A8 8 0 0 1 4.1 10L9 15v1a2 2 0 0 0 2 2zm6.9-2.5A2 2 0 0 0 16 16h-1v-3a1 1 0 0 0-1-1H8v-2h2a1 1 0 0 0 1-1V7h2a2 2 0 0 0 2-2v-.4a8 8 0 0 1 2.9 12.8z"/></svg>
        solacegrove.net
      </li>
    </ul>
    <address class="practitioner">
      Marnie Toller D.C., L.Ac., MSOM<br>
      584 W 12th St, Ste 320<br>
      Larkfield, NE 68419
    </address>
  </section>

  <section class="card card--back">
    <div class="wordmark">
      <span class="wordmark__name">Solace</span>
      <span class="wordmark__tagline">Chiropractic &amp; Acupuncture</span>
    </div>
  </section>
</main>
</body>
</html>
```